Pharmacy

Two sided postcard. Pictures on one side. Description on the other. We design and build pharmacies. pictures are some of our finished work. You can use as many pictures as you like not necessary to use all of them. Size of card should be 5"x7". See my website at display@brightfieldfixtures.com for more inspiration. I include the back of one card that I used recently. Both sids need design input. Feel free to contact me with questions.
Requirements
Must have
- Must be a two sided postcard
Nice to have
- I am sending a design of a sleek type postcard that I saw online as an example.
- https://lnk.example-pics.net/images/q7KmRz
- I am looking for something modern.
- Not limited to colors on my website.

```html
<!DOCTYPE html>
<html lang="en">
<head>
<meta charset="utf-8">
<title>Brightfield Showcase &amp; Store Fixture Co. Inc – Postcard</title>
<link rel="stylesheet" href="https://fonts.googleapis.com/css2?family=Tinos&family=Arimo:wght@400;700&display=swap">
<style>
  :root {
    --brown-dark: #4a2f24;
    --teal: #4e96a0;
    --grey-warm: #8c8885;
    --copper: #b27b3c;
    --panel: #e9e7e6;
    --ink: #111111;
    --white: #ffffff;
    --phone-band: #1f3a3d;
    --link-orange: #f0a11f;
    --frame: #d7d2cd;
    --photo-wood: #8a5030;
    --photo-cream: #d9cbb8;
    --photo-shelf: #b99a7e;
  }
  * { margin: 0; padding: 0; box-sizing: border-box; }
  html, body { width: 1200px; height: 857px; overflow: hidden; }
  .postcard {
    position: relative;
    width: 1200px;
    height: 857px;
    overflow: hidden;
    background:
      linear-gradient(180deg, rgba(0,0,0,0) 0%, rgba(0,0,0,0) 70%, rgba(140,100,55,0.85) 100%),
      linear-gradient(90deg, #6c6865 0%, var(--brown-dark) 28%, #6b4a3b 45%, var(--teal) 62%, #7d8a8a 78%, #8f7a66 100%);
    font-family: "Arimo", Arial, sans-serif;
  }
  .company-title {
    position: absolute;
    left: 0; top: 44px;
    width: 612px;
    text-align: center;
    font-family: "Tinos", "Times New Roman", serif;
    font-weight: 400;
    font-size: 51px;
    line-height: 56px;
    color: var(--white);
  }
  .tagline-band {
    position: absolute;
    left: 0; top: 190px;
    width: 600px; height: 102px;
    background: var(--copper);
    display: flex; align-items: center; justify-content: center;
  }
  .tagline {
    font-weight: 700;
    font-size: 34px;
    color: var(--white);
  }
  .about-panel {
    position: absolute;
    left: 0; top: 342px;
    width: 600px; height: 291px;
    background: var(--panel);
    padding: 30px 30px 0 30px;
  }
  .about-text {
    font-size: 17.5px;
    line-height: 42.5px;
    color: var(--ink);
    text-align: justify;
    text-align-last: left;
  }
  .phone-band {
    position: absolute;
    left: 0; top: 662px;
    width: 600px; height: 74px;
    background: linear-gradient(90deg, rgba(31,58,61,0) 0%, var(--phone-band) 20%, var(--phone-band) 80%, rgba(31,58,61,0) 100%);
    display: flex; align-items: center; justify-content: center;
  }
  .phone {
    font-weight: 700;
    font-size: 36px;
    color: var(--white);
    letter-spacing: 0.5px;
  }
  .web-links {
    position: absolute;
    left: 0; top: 748px;
    width: 600px;
    text-align: center;
    font-weight: 700;
    font-size: 24px;
    line-height: 31px;
    color: var(--link-orange);
  }
  .gallery {
    position: absolute;
    left: 600px; top: 8px;
    width: 588px; height: 842px;
  }
  .overlay-lines {
    position: absolute;
    color: var(--white);
    font-weight: 700;
  }
  .overlay-lines span {
    display: block;
    width: max-content;
    padding: 0 4px;
    background: rgba(40,40,40,0.35);
    border-radius: 6px;
  }
  .postage-indicia {
    left: 1036px; top: 22px;
    font-size: 19px;
    line-height: 31px;
  }
  .return-address {
    left: 636px; top: 697px;
    font-size: 18px;
    line-height: 31px;
  }
</style>
</head>
<body>
<main class="postcard">
  <h1 class="company-title">Brightfield Showcase &amp;<br>Store Fixture Co. Inc</h1>

  <div class="tagline-band">
    <p class="tagline">Quality - Experience - Innovation</p>
  </div>

  <section class="about-panel">
    <p class="about-text">Family owned ad operated for three geertions - Brightfield Showcase &amp; Store Fixture Co. Inc is the oldest store fixture company In New jersey.As designers &amp; Maufacturers we can sae you hours of time ad money. Our level of experience will be evident from the outset ad you will be pleased that you found us</p>
  </section>

  <div class="phone-band">
    <p class="phone">201 555 0148</p>
  </div>

  <p class="web-links">display@brightfieldfixtures.com<br>www.brightfieldfixtures.com</p>

  <svg class="gallery" viewBox="0 0 588 842" xmlns="http://www.w3.org/2000/svg">
    <defs>
      <linearGradient id="shelfWood" x1="0" y1="0" x2="1" y2="1">
        <stop offset="0" stop-color="#c9b9a6"/>
        <stop offset="0.55" stop-color="#9a6a48"/>
        <stop offset="1" stop-color="#6f3e22"/>
      </linearGradient>
      <linearGradient id="counterLight" x1="0" y1="0" x2="1" y2="1">
        <stop offset="0" stop-color="#7d5a44"/>
        <stop offset="0.5" stop-color="#c7b8a8"/>
        <stop offset="1" stop-color="#8f6a50"/>
      </linearGradient>
      <linearGradient id="aisleCool" x1="0" y1="0" x2="1" y2="1">
        <stop offset="0" stop-color="#d6d6d8"/>
        <stop offset="0.6" stop-color="#8f9aa6"/>
        <stop offset="1" stop-color="#4c5560"/>
      </linearGradient>
      <linearGradient id="centerStore" x1="0" y1="0" x2="0" y2="1">
        <stop offset="0" stop-color="#c9a88a"/>
        <stop offset="0.5" stop-color="#7a4a2e"/>
        <stop offset="1" stop-color="#d3c8bc"/>
      </linearGradient>
    </defs>
    <rect x="2" y="2" width="584" height="838" rx="40" fill="none" stroke="var(--frame)" stroke-width="5"/>
    <rect role="img" aria-label="Photo: pharmacy aisle with curved wood end shelving stocked with baby care products" x="16" y="16" width="268" height="400" rx="30" fill="url(#shelfWood)" stroke="var(--frame)" stroke-width="6"/>
    <rect role="img" aria-label="Photo: pharmacy counter with marble top and wood shelving behind" x="304" y="16" width="268" height="400" rx="30" fill="url(#counterLight)" stroke="var(--frame)" stroke-width="6"/>
    <rect role="img" aria-label="Photo: bright pharmacy aisle with slatwall displays of first aid goods" x="16" y="424" width="268" height="404" rx="30" fill="url(#aisleCool)" stroke="var(--frame)" stroke-width="6"/>
    <rect role="img" aria-label="Photo: wood end shelving with baby care products on tiled floor" x="304" y="424" width="268" height="404" rx="30" fill="url(#shelfWood)" stroke="var(--frame)" stroke-width="6"/>
    <polygon role="img" aria-label="Photo: fragrance glass showcase in front of tall wood wall shelving" points="292,200 508,416 292,632 76,416" fill="url(#centerStore)" stroke="var(--frame)" stroke-width="6" stroke-linejoin="round"/>
  </svg>

  <div class="overlay-lines postage-indicia">
    <span>presorted</span>
    <span>FIRST CLASS</span>
    <span>US POSTAGE</span>
    <span>PAID</span>
    <span>Postline</span>
  </div>

  <div class="overlay-lines return-address">
    <span>Brightfield showcase &amp;</span>
    <span>Store Fixture Co. Inc</span>
    <span>PO Box 418</span>
    <span>Ridgefield NJ 07657</span>
  </div>
</main>
</body>
</html>
```